Business Card Design

We have our logo and everything in place. Looking to have a layout for our new business cards designed. These will be printed with a matte finish, possibly rounded corners, and looking to incorporate some cool spot UV layers into the design.

Ive uploaded the existing card front and back as well as our logo.

Card Size Will Be 3.5" x 2"

```html
<!DOCTYPE html>
<html lang="en">
<head>
<meta charset="utf-8">
<title>Larchwood Deck and Rail – Business Card</title>
<link rel="stylesheet" href="https://fonts.googleapis.com/css2?family=Libre+Baskerville:ital,wght@0,400;0,700;1,400&display=swap">
<style>
  :root {
    --card-bg: #111314;
    --card-bg-soft: #1c1f21;
    --ink: #ffffff;
    --accent: #3fa0e0;
  }
  html, body {
    margin: 0;
    padding: 0;
    width: 1200px;
    height: 686px;
    overflow: hidden;
    background: var(--card-bg);
  }
  .card {
    position: relative;
    width: 1200px;
    height: 686px;
    overflow: hidden;
    font-family: "Libre Baskerville", Georgia, serif;
    color: var(--ink);
  }
  .card__texture {
    position: absolute;
    inset: 0;
    width: 100%;
    height: 100%;
  }
  .card__divider {
    position: absolute;
    left: 623px;
    top: 0;
    width: 2px;
    height: 686px;
    background: var(--ink);
  }
  .brand {
    position: absolute;
    left: 0;
    top: 250px;
    width: 624px;
    text-align: center;
    font-weight: 400;
    color: var(--ink);
  }
  .brand__name {
    font-size: 82px;
    line-height: 1;
    margin: 0;
    font-weight: 400;
  }
  .brand__trade {
    margin: 34px 0 0;
    font-size: 34px;
    letter-spacing: 4px;
    font-weight: 400;
  }
  .contact {
    position: absolute;
    left: 642px;
    top: 250px;
    width: 545px;
  }
  .contact__name {
    margin: 0;
    font-size: 42px;
    font-weight: 400;
    letter-spacing: 4px;
    line-height: 1;
  }
  .contact__role {
    margin: 14px 0 0;
    font-size: 27px;
    letter-spacing: 1.5px;
    color: var(--accent);
    line-height: 1;
  }
  .contact__phone,
  .contact__email {
    margin: 0;
    font-style: italic;
    font-size: 26px;
    letter-spacing: 2px;
    line-height: 1;
  }
  .contact__phone { margin-top: 52px; }
  .contact__email { margin-top: 12px; font-size: 24px; letter-spacing: 1.6px; }
  .contact__web {
    position: absolute;
    left: 652px;
    top: 553px;
    margin: 0;
    font-size: 27px;
    letter-spacing: 2px;
    line-height: 1;
  }
</style>
</head>
<body>
  <main class="card">
    <svg class="card__texture" viewBox="0 0 1200 686" preserveAspectRatio="none" role="img" aria-label="Faint dark damask flourish pattern across the card background">
      <defs>
        <radialGradient id="texture-glow" cx="50%" cy="45%" r="75%">
          <stop offset="0%" stop-color="#1c1f21"/>
          <stop offset="100%" stop-color="#111314"/>
        </radialGradient>
      </defs>
      <rect width="1200" height="686" fill="url(#texture-glow)"/>
    </svg>

    <div class="card__divider"></div>

    <section class="brand" aria-label="Company name">
      <p class="brand__name">Larchwood</p>
      <p class="brand__trade">DECK AND RAIL</p>
    </section>

    <section class="contact">
      <h1 class="contact__name">CALEB WARDELL</h1>
      <p class="contact__role">President</p>
      <p class="contact__phone">403.555.0187</p>
      <p class="contact__email">larchwooddeckandrail@mail.com</p>
    </section>

    <p class="contact__web">www.larchwooddeckandrail.com</p>
  </main>
</body>
</html>
```